Computer consultant business card

Brimlo Software is a newly started computer consulting company. It's a small one-man company that provides mostly Velunix applications but also websites in collaboration with designers. I'm running this company on the side of full time university studies.

I want the final design to be clean and memorable. Be creative! :)

Some inspiration:
http://www.tavelpix.net/design/73519
http://www.tavelpix.net/design/2739566/business-card-design-by-quillbop
http://www.tavelpix.net/design/804613/business-card-design-by-lorvena-brukwaldsen

See attachment for my company logo.
Updates

I would like to thank everyone for submitting! I'll need a couple of days to review and ultimately select a design.

Target Market(s)

Non-technical entrepreneurs and small companies.

Industry/Entity Type

University

Requirements
Must have
• My company logo.
In any way, both colors from my logo.
First- and last name, e-mail and phone number.
Double-sided design.
Nice to have
• Something creative with the symbol in my logo

```html
<!DOCTYPE html>
<html lang="en">
<head>
<meta charset="utf-8">
<title>Brimlo Software – Business Card</title>
<link rel="stylesheet" href="https://fonts.googleapis.com/css2?family=Jost:wght@300;400;500&display=swap">
<style>
  :root {
    --page-bg: #2f3a3b;
    --card-top: #30323f;
    --card-bottom: #1c1d28;
    --band-light: #d9dbe0;
    --band-light-edge: #9fa3b0;
    --band-blue: #7f8fd0;
    --band-blue-deep: #4e5a94;
    --text-light: #d6d9e2;
    --text-soft: #a9adbb;
  }
  * { margin: 0; padding: 0; box-sizing: border-box; }
  html, body {
    width: 1200px;
    height: 1000px;
    overflow: hidden;
    background: var(--page-bg);
    font-family: "Jost", "Futura", sans-serif;
  }
  .sheet {
    position: relative;
    width: 1200px;
    height: 1000px;
  }
  .card {
    position: absolute;
    left: 200px;
    width: 800px;
    height: 340px;
    overflow: hidden;
    box-shadow: 0 10px 28px rgba(0, 0, 0, 0.45);
  }
  .card--front { top: 80px; }
  .card--back  { top: 570px; }
  .card__art {
    position: absolute;
    inset: 0;
    width: 800px;
    height: 340px;
  }
  .card__content {
    position: absolute;
    left: 280px;
    top: 20px;
    width: 300px;
    height: 300px;
    display: flex;
    flex-direction: column;
    align-items: center;
    justify-content: center;
    text-align: center;
  }
  .brand-name {
    font-size: 78px;
    font-weight: 500;
    color: var(--text-light);
    letter-spacing: 1px;
    line-height: 1;
  }
  .person-name {
    font-size: 33px;
    font-weight: 300;
    color: var(--text-soft);
    letter-spacing: 2px;
    text-transform: uppercase;
    margin-bottom: 14px;
    white-space: nowrap;
  }
  .contact-list {
    list-style: none;
    font-size: 13px;
    font-weight: 400;
    color: var(--text-soft);
    letter-spacing: 1px;
    line-height: 1.25;
    text-transform: uppercase;
  }
</style>
</head>
<body>
<main class="sheet">

  <section class="card card--front" aria-label="Card front">
    <svg class="card__art" viewBox="0 0 800 340" aria-hidden="true">
      <defs>
        <linearGradient id="front-bg" x1="0" y1="0" x2="0" y2="1">
          <stop offset="0" stop-color="var(--card-top)"/>
          <stop offset="1" stop-color="var(--card-bottom)"/>
        </linearGradient>
        <linearGradient id="front-light" x1="0" y1="0" x2="0" y2="1">
          <stop offset="0" stop-color="var(--band-light)"/>
          <stop offset="1" stop-color="var(--band-light-edge)"/>
        </linearGradient>
        <linearGradient id="front-blue" x1="0" y1="0" x2="0" y2="1">
          <stop offset="0" stop-color="var(--band-blue)"/>
          <stop offset="1" stop-color="var(--band-blue-deep)"/>
        </linearGradient>
      </defs>
      <rect width="800" height="340" fill="url(#front-bg)"/>
      <polygon class="band band--light" points="230,0 300,0 240,340 170,340" fill="url(#front-light)"/>
      <polygon class="band band--blue" points="620,0 690,0 630,340 560,340" fill="url(#front-blue)"/>
    </svg>
    <div class="card__content">
      <p class="brand-name">brimlo</p>
    </div>
  </section>

  <section class="card card--back" aria-label="Card back">
    <svg class="card__art" viewBox="0 0 800 340" aria-hidden="true">
      <defs>
        <linearGradient id="back-bg" x1="0" y1="0" x2="0" y2="1">
          <stop offset="0" stop-color="var(--card-top)"/>
          <stop offset="1" stop-color="var(--card-bottom)"/>
        </linearGradient>
        <linearGradient id="back-light" x1="0" y1="0" x2="0" y2="1">
          <stop offset="0" stop-color="var(--band-light)"/>
          <stop offset="1" stop-color="var(--band-light-edge)"/>
        </linearGradient>
        <linearGradient id="back-blue" x1="0" y1="0" x2="0" y2="1">
          <stop offset="0" stop-color="var(--band-blue)"/>
          <stop offset="1" stop-color="var(--band-blue-deep)"/>
        </linearGradient>
      </defs>
      <rect width="800" height="340" fill="url(#back-bg)"/>
      <polygon class="band band--light" points="230,0 300,0 240,340 170,340" fill="url(#back-light)"/>
      <polygon class="band band--blue" points="620,0 690,0 630,340 560,340" fill="url(#back-blue)"/>
    </svg>
    <div class="card__content">
      <h1 class="person-name">Tom Hadley</h1>
      <ul class="contact-list">
        <li class="contact-list__web">brimlo.com</li>
        <li class="contact-list__email">tomhadley@brimlo.com</li>
        <li class="contact-list__phone">01632 960481</li>
      </ul>
    </div>
  </section>

</main>
</body>
</html>
```